Innovative Australian Importation company in Sustainability space needs beautiful website*

We seek your services to provide a clean, modern we rendered logo for or company Red Fern Coastal Supply Pty Ltd, this will be used in all the usual places however you will aso build us our business cards and our website: redferncoastalsupply.example

What we do:
We source innovative products that solve problems in the Aeroponics, Hydroponics, Horticultural, Organics and sustainability space. We source our product from all over the world however our cliant base is predominantly in Australia & New Zealand Region.
Our company's mission is to help retail businesses by providing high-quality products at a competitive price for everyday people to produce healthy sustainable consumables from home, making it easy for the end-user to become more self-sufficient with while remaining environmentally friendly.

Target Market(s)

Aeroponics, Hydroponics, Horticultural, Organics and sustainability space.

Industry/Entity Type

Wholesale

Contact Information for Business Card

We would like these to be very modern and glossy possibly an embosed logo or rounded edges, a little smaller than the traditional?

Logo Text

Red Fern Coastal Supply

Coding

Coded - Design and coding required

Number of Pages Required

1 page

Colors
0355a3

Requirements
Must have
• The websit is bit of a landing page that will provide some minor information on our imported products. and qualify resellers ( Our target Market) from retail clients (the end-user) and provide a private store and check out for our trade customers. (not for Reatil)
Abillity to set up a trade account (must have our approval befor being granted access to shop.)
the abillity to for OEM's and International wholsalers register intrest.
The abillity to register/inquire about our produtc lines for Retailer.
The abillity to provide the end-user a list of resellers.
The ability for promo video
Nice to have
• .
Should not have
• Logo high gloss, 3d rendered

```html
<!DOCTYPE html>
<html lang="en">
<head>
<meta charset="utf-8">
<title>Red Fern Coastal Supply</title>
<link href="https://fonts.googleapis.com/css2?family=Poppins:wght@600;700&family=Roboto:wght@400;500;700&display=swap" rel="stylesheet">
<style>
:root{
  --navy:#233e80;
  --navy-dark:#1d3470;
  --sky:#1aa7ec;
  --ink:#1a1a1a;
  --text:#666;
  --beige:#f6f5f1;
  --grey-bg:#f4f4f4;
  --footer:#1c1d22;
  --star:#f5b301;
}
*{margin:0;padding:0;box-sizing:border-box}
html,body{width:1200px;height:4120px;overflow:hidden;background:#fff}
body{position:relative;font-family:"Roboto",sans-serif;color:var(--ink)}
.abs{position:absolute}
h2{font-family:"Poppins",sans-serif;font-weight:700;color:var(--ink);text-align:center}
/* header */
.brand{left:110px;top:28px;display:flex;align-items:center;gap:12px}
.brand-dot{width:54px;height:54px;border-radius:50%;background:var(--navy)}
.brand-name{font-weight:700;font-size:15px;color:var(--navy)}
.brand-tag{font-size:9.5px;color:#555;margin-top:5px}
.top-tabs{left:742px;top:0;height:40px;display:flex}
.tab{height:40px;line-height:40px;color:#fff;font-weight:700;font-size:14px;padding:0 30px;clip-path:polygon(12px 0,100% 0,calc(100% - 12px) 100%,0 100%)}
.tab.trade{background:var(--navy);padding:0 30px 0 32px}
.tab.reg{background:var(--sky);margin-left:-8px;padding:0 50px 0 48px}
.nav{left:441px;top:70px;display:flex;gap:27px;font-weight:700;font-size:14px}
.nav a{color:var(--ink);text-decoration:none;padding-bottom:8px}
.nav a.active{color:var(--sky);border-bottom:3px solid var(--sky)}
.call{left:898px;top:62px;display:flex;align-items:center;gap:14px}
.call .sep{width:1px;height:36px;background:#ddd}
.call small{font-size:10px;font-weight:500;display:block}
.call b{font-size:21px;font-weight:700}
/* hero */
.hero{left:0;top:110px;width:1200px;height:590px;background:linear-gradient(180deg,#8fa084 0%,#6c8a3f 35%,#5d8a2a 70%,#3d5c1f 100%)}
.hero-title{left:0;top:292px;width:1200px;text-align:center;font-family:"Poppins",sans-serif;font-weight:700;font-size:36px;line-height:45px;color:#fff}
.hero-sub{left:0;top:404px;width:1200px;text-align:center;font-size:17px;color:#fff}
.btn{display:inline-flex;align-items:center;gap:8px;justify-content:center;color:#fff;background:var(--sky);border-radius:30px;font-weight:700;font-size:15px}
.hero-btn{left:500px;top:455px;width:200px;height:50px}
.arrow{width:40px;height:40px;border:2px solid #fff;border-radius:50%;top:385px}
/* products */
.section-title{font-size:32px;line-height:40px}
.card{overflow:hidden}
.card .img{position:absolute;left:0;top:0;right:0;height:245px}
.card .label{position:absolute;left:0;bottom:0;right:0;height:50px;line-height:50px;text-align:center;color:#fff;font-weight:700;font-size:18px;background:var(--navy)}
.card .label::before{content:"";position:absolute;left:50%;top:-12px;margin-left:-12px;border:12px solid transparent;border-top:0;border-bottom-color:inherit}
.card .label.navy{border-bottom-color:var(--navy)}
.card .label.sky{background:var(--sky);border-bottom-color:var(--sky)}
/* about */
.about-bg{left:0;top:1646px;width:1200px;height:317px;background:var(--beige)}
.navy-bg{left:0;top:1963px;width:1200px;height:655px;background:var(--navy)}
.about-text{left:220px;top:1744px;width:760px;text-align:center;font-size:15px;line-height:26px;color:var(--text)}
.video{left:205px;top:1861px;width:791px;height:422px;background:linear-gradient(135deg,#c9b29a 0%,#eae6df 40%,#7aa34a 70%,#dcdcd6 100%)}
.play{left:562px;top:2035px;width:76px;height:76px;border-radius:50%;background:var(--sky)}
.why{color:#fff}
.feature{width:224px;text-align:center;color:#fff;font-weight:700;font-size:16px}
.feature .ring{width:96px;height:96px;margin:0 auto 18px;border-radius:50%;background:#fff;border:4px solid var(--navy-dark);box-shadow:0 0 0 3px #fff;display:flex;align-items:center;justify-content:center}
/* resellers */
.res-img{left:110px;top:2725px;width:540px;height:341px;background:linear-gradient(160deg,#e4e8ea 0%,#a9c48a 50%,#5e8c33 100%)}
.res-card{left:565px;top:2770px;width:539px;height:355px;background:#fff;box-shadow:0 4px 20px rgba(0,0,0,.08);border-right:4px solid var(--sky);padding:40px 35px}
.res-card h3{font-family:"Poppins",sans-serif;font-weight:700;font-size:32px;margin-bottom:16px}
.res-card p{font-size:15px;line-height:27px;color:var(--text);margin-bottom:10px}
.res-card .btn{width:177px;height:46px;margin-top:12px;font-size:14px}
/* testimonials */
.test-bg{left:0;top:3233px;width:1200px;height:524px;background:var(--grey-bg)}
.quote{width:311px;height:188px;background:#fff;border-top:3px solid var(--sky);border-radius:8px;padding:70px 26px 0;text-align:center;font-size:14px;line-height:25.5px;color:#444}
.avatar{width:92px;height:92px;border-radius:50%;background:#d8d2cb;border:4px solid #fff}
.who{width:311px;text-align:center;font-size:15px;font-weight:700}
.who span{font-size:10px;font-weight:400;color:#555}
.stars{width:311px;text-align:center;color:var(--star);font-size:14px;letter-spacing:1px}
/* footer */
.footer{left:0;top:3757px;width:1200px;height:363px;background:var(--footer);color:#fff}
.f-dot{left:192px;top:3830px;width:60px;height:60px;border-radius:50%;background:var(--navy)}
.f-name{left:110px;top:3908px;width:224px;text-align:center;font-weight:700;font-size:15px;color:var(--sky)}
.f-tag{left:110px;top:3934px;width:224px;text-align:center;font-size:10px}
.f-social{left:166px;top:3983px;display:flex;gap:18px}
.f-social i{display:block;width:14px;height:14px;border-radius:50%;background:#fff}
.f-h{font-weight:700;font-size:16px}
.f-item{font-size:13px;line-height:19px}
.f-item b{font-size:11px;display:block}
.f-links{font-size:13px;line-height:25.6px}
.f-btn{left:862px;top:3955px;width:198px;height:42px;font-size:14px}
.f-rule{left:110px;top:4044px;width:978px;height:1px;background:#33343a}
.goup{left:1008px;top:4027px;width:80px;height:20px;border-radius:10px;background:#eee;color:#222;font-size:10px;font-weight:700;text-align:center;line-height:20px}
.f-bottom{top:4080px;font-size:13px}
</style>
</head>
<body>

<!-- Header -->
<div class="abs brand">
  <div class="brand-dot"></div>
  <div><div class="brand-name">RED FERN COASTAL SUPPLY</div><div class="brand-tag">Connecting your Business to a world of products</div></div>
</div>
<div class="abs top-tabs"><div class="tab trade">TRADE ACCOUNT</div><div class="tab reg">REGISTER</div></div>
<nav class="abs nav"><a class="active">HOME</a><a>ABOUT US</a><a>PRODUCTS</a><a>BLOG</a><a>CONTACT US</a></nav>
<div class="abs call">
  <svg width="24" height="24" viewBox="0 0 24 24" fill="none" stroke="#888" stroke-width="1.6"><path d="M5 3h4l2 5-2.5 1.5a11 11 0 0 0 6 6L16 13l5 2v4a2 2 0 0 1-2 2A16 16 0 0 1 3 5a2 2 0 0 1 2-2z"/></svg>
  <div class="sep"></div>
  <div><small>CALL US</small><b>555 017 2046</b></div>
</div>

<!-- Hero -->
<div class="abs hero" role="img" aria-label="Greenhouse with rows of hydroponic lettuce"></div>
<div class="abs hero-title">Connecting your Business to<br>a world of products</div>
<div class="abs hero-sub">Lorem ipsum dolor sit amet, consectetur adipiscing elit.</div>
<div class="abs btn hero-btn">GET STARTED
  <svg width="15" height="15" viewBox="0 0 16 16"><circle cx="8" cy="8" r="8" fill="#fff"/><path d="M6 4.5 9.5 8 6 11.5" stroke="#1aa7ec" stroke-width="2" fill="none"/></svg></div>
<svg class="abs arrow" style="left:32px" viewBox="0 0 40 40"><path d="M23 13l-7 7 7 7" stroke="#fff" stroke-width="2" fill="none"/></svg>
<svg class="abs arrow" style="left:1128px" viewBox="0 0 40 40"><path d="M17 13l7 7-7 7" stroke="#fff" stroke-width="2" fill="none"/></svg>

<!-- Products -->
<h2 class="abs section-title" style="left:0;top:802px;width:1200px">Innovative products that solve<br>problems in</h2>
<div class="abs card" style="left:110px;top:927px;width:312px;height:295px">
  <div class="img" role="img" aria-label="Aeroponic towers under pink grow lights" style="background:linear-gradient(180deg,#7d4a5c,#c9667e 60%,#4a3c3c)"></div>
  <div class="label navy">Aeroponics</div></div>
<div class="abs card" style="left:445px;top:927px;width:310px;height:295px">
  <div class="img" role="img" aria-label="Hands holding a hydroponic lettuce with roots" style="background:linear-gradient(160deg,#d9e6d6,#7fb24a 50%,#5b7f3a)"></div>
  <div class="label sky">Hydroponics</div></div>
<div class="abs card" style="left:777px;top:927px;width:311px;height:295px">
  <div class="img" role="img" aria-label="Gardener tending seedlings in a greenhouse" style="background:linear-gradient(180deg,#e8ebea,#b5c6a7 55%,#6f8e55)"></div>
  <div class="label navy">Horticultural</div></div>
<div class="abs card" style="left:110px;top:1245px;width:479px;height:295px">
  <div class="img" role="img" aria-label="Crate of fresh organic vegetables in a field" style="background:linear-gradient(180deg,#7e8a4a,#b59a6a 50%,#8a6d4a)"></div>
  <div class="label navy">Organics</div></div>
<div class="abs card" style="left:611px;top:1245px;width:477px;height:295px">
  <div class="img" role="img" aria-label="Seedling sprouting from dark soil" style="background:linear-gradient(180deg,#9cc94f,#78b038 60%,#1f1d16 78%)"></div>
  <div class="label navy">Sustainability Space</div></div>

<!-- About -->
<div class="abs about-bg"></div>
<div class="abs navy-bg"></div>
<h2 class="abs" style="left:0;top:1670px;width:1200px;font-size:38px">About Us</h2>
<p class="abs about-text">Our company's mission is to help retail businesses by providing high-quality products at a competitive price for everyday people to produce healthy sustainable consumables from home, making it easy for the end-user to become more self-sufficient while remaining environmentally friendly.</p>
<div class="abs video" role="img" aria-label="Promo video still: hand placing a seedling into a hydroponic tray"></div>
<svg class="abs play" viewBox="0 0 76 76"><circle cx="38" cy="38" r="38" fill="#1aa7ec"/><path d="M31 26l18 12-18 12z" fill="#fff"/></svg>
<h2 class="abs why" style="left:0;top:2337px;width:1200px;font-size:38px;color:#fff">Why Choose Us?</h2>

<div class="abs feature" style="left:164px;top:2422px"><div class="ring">
  <svg width="48" height="52" viewBox="0 0 48 52" fill="none" stroke="#233e80" stroke-width="2"><circle cx="24" cy="18" r="14"/><path d="M24 32v14M19 41l5 5 5-5M28 12h-6a3 3 0 0 0 0 6h4a3 3 0 0 1 0 6h-6M24 9v3M24 24v3"/></svg>
  </div>Save 33% on costs</div>
<div class="abs feature" style="left:388px;top:2422px"><div class="ring">
  <svg width="52" height="52" viewBox="0 0 52 52" fill="none" stroke="#233e80" stroke-width="2"><circle cx="28" cy="29" r="16"/><path d="M28 9v4M24 9h8M28 29l6-6M4 24h8M2 30h10M6 36h8"/></svg>
  </div>4x Faster</div>
<div class="abs feature" style="left:611px;top:2422px"><div class="ring">
  <svg width="46" height="52" viewBox="0 0 46 52" fill="none" stroke="#233e80" stroke-width="2"><rect x="6" y="4" width="34" height="30"/><path d="M6 24v24h34V24M6 48l17-13 17 13"/><rect x="12" y="12" width="22" height="8"/></svg>
  </div>Compliance Ready</div>
<div class="abs feature" style="left:836px;top:2422px"><div class="ring">
  <svg width="50" height="48" viewBox="0 0 50 48" fill="none" stroke="#233e80" stroke-width="2"><path d="M10 18h30l6 8-21 18L4 26z M4 26h42 M18 18l7 26 7-26"/><path d="M25 4v8M14 7l4 6M36 7l-4 6" stroke="#1aa7ec"/></svg>
  </div>Simple</div>

<!-- Resellers -->
<div class="abs res-img" role="img" aria-label="Worker checking plant racks in a greenhouse"></div>
<div class="abs res-card">
  <h3>Qualify Resellers</h3>
  <p>Lorem ipsum dolor sit amet, consectetur adipiscing elit, sed do eiusmod tempor incididunt ut labore et dolore magna aliqua. Ut enim ad minim veniam, quis nostrud exercitation</p>
  <p>Duis aute irure dolor in reprehenderit in voluptate velit esse cillum dolore eu fugiat nulla pariatur.</p>
  <div class="btn">LEARN MORE
    <svg width="15" height="15" viewBox="0 0 16 16"><circle cx="8" cy="8" r="8" fill="#fff"/><path d="M6 4.5 9.5 8 6 11.5" stroke="#1aa7ec" stroke-width="2" fill="none"/></svg></div>
</div>

<!-- Testimonials -->
<div class="abs test-bg"></div>
<h2 class="abs" style="left:0;top:3280px;width:1200px;font-size:34px">What Our clients say?</h2>

<div class="abs quote" style="left:110px;top:3397px">"Lorem ipsum dolor amet, consectetur adipiscing elit, sed do eiusmod tempor incididunt ut labore et dolore magna aliqua. Ut enim ad minim veniam,</div>
<div class="abs avatar" role="img" aria-label="Client portrait" style="left:219px;top:3349px"></div>
<div class="abs who" style="left:110px;top:3606px">Mara Quill, <span>Newport, NSW</span></div>
<div class="abs stars" style="left:110px;top:3630px">★★★★★</div>

<div class="abs quote" style="left:445px;top:3397px">"Lorem ipsum dolor amet, consectetur adipiscing elit, sed do eiusmod tempor incididunt ut labore et dolore magna aliqua. Ut enim ad minim veniam,</div>
<div class="abs avatar" role="img" aria-label="Client portrait" style="left:554px;top:3349px"></div>
<div class="abs who" style="left:445px;top:3606px">Tobin Reyes, <span>Nelson, NZ</span></div>
<div class="abs stars" style="left:445px;top:3630px">★★★★★</div>

<div class="abs quote" style="left:777px;top:3397px">"Lorem ipsum dolor amet, consectetur adipiscing elit, sed do eiusmod tempor incididunt ut labore et dolore magna aliqua. Ut enim ad minim veniam,</div>
<div class="abs avatar" role="img" aria-label="Client portrait" style="left:886px;top:3349px"></div>
<div class="abs who" style="left:777px;top:3606px">Ade Okafor, <span>Byron Bay, NSW</span></div>
<div class="abs stars" style="left:777px;top:3630px">★★★★★</div>

<!-- Footer -->
<div class="abs footer"></div>
<div class="abs f-dot"></div>
<div class="abs f-name">RED FERN COASTAL SUPPLY</div>
<div class="abs f-tag">Connecting your Business to a world of products</div>
<div class="abs f-social"><i></i><i></i><i></i><i></i></div>

<div class="abs f-h" style="left:412px;top:3820px;color:#fff">Our Office Address</div>
<svg class="abs" style="left:412px;top:3862px" width="12" height="12" viewBox="0 0 24 24" fill="#1aa7ec"><path d="M5 2h4l2 6-3 2a12 12 0 0 0 6 6l2-3 6 2v4a3 3 0 0 1-3 3A19 19 0 0 1 2 5a3 3 0 0 1 3-3z"/></svg>
<div class="abs f-item" style="left:435px;top:3859px;color:#fff"><b>Phone</b>555-014-3382</div>
<svg class="abs" style="left:412px;top:3916px" width="13" height="10" viewBox="0 0 26 20" fill="#1aa7ec"><rect width="26" height="20" rx="2"/><path d="M1 2l12 9 12-9" stroke="#1c1d22" stroke-width="2" fill="none"/></svg>
<div class="abs f-item" style="left:435px;top:3911px;color:#fff"><b>Email</b>info@redferncoastalsupply.example</div>
<svg class="abs" style="left:412px;top:3970px" width="11" height="14" viewBox="0 0 22 28" fill="#1aa7ec"><path d="M11 0a11 11 0 0 1 11 11c0 8-11 17-11 17S0 19 0 11A11 11 0 0 1 11 0z"/><circle cx="11" cy="11" r="4" fill="#1c1d22"/></svg>
<div class="abs f-item" style="left:435px;top:3966px;color:#fff"><b>Location</b>123, Lorem ipsum dolor amet,<br>consectetur elit</div>

<div class="abs f-h" style="left:697px;top:3820px;color:#fff">Company</div>
<div class="abs f-links" style="left:697px;top:3858px;color:#fff">Home<br>About us<br>Products<br>Promo<br>Contact us</div>

<div class="abs f-h" style="left:862px;top:3820px;color:#fff">Stil have questios?</div>
<div class="abs f-item" style="left:862px;top:3861px;width:240px;font-size:12px;color:#fff">Contact us using this form. A repesenta-tive will aswer your questions as soon as possible.</div>
<div class="abs btn f-btn">GET IN TOUCH</div>

<div class="abs goup">↑ Go Up</div>
<div class="abs f-rule"></div>
<div class="abs f-bottom" style="left:110px;color:#fff">© 2020 redferncoastalsupply.example | All Rights Reserved</div>
<div class="abs f-bottom" style="left:769px;color:#fff">Privacy Policy &nbsp;|&nbsp; Disclaimer &nbsp;|&nbsp; Terms Of Services</div>

</body>
</html>
```